Velvet Horizon Voyages Inc. We are looking for a skilled designer for our new Logo, Letterhead and Biz Car

We are looking for a fresh logo design for our new travel business. We excel in maximizing reward points for our clients that are high limit spenders or business owners, that can accumulate above average pools of airline, bank and travel points. Our core sales are in personal travel that crosses-over to business travel. Luxury Travel images and themes are essential in the design of the logo and biz cards. The letterhead can remain clean and refined.

Target Market(s)

Luxury Travelers and Business Owners that use reward point credit cards and programs to enhance their travel experiences.

Industry/Entity Type

Travel

Contact Information for Business Card

212 Pinecrest Hollow Rd NW
Calgary, Alberta T2K 4W9 Canada
Tel: (403)271-4408
kdelane@velvethorizonvoyages.com
www.velvethorizonvoyages.com

Logo Text

Velvet Horizon Voyages Inc.

Requirements
Must have
• Luxury Travel Image(s) or original stylized versions of that.
• Add supplier logo for: Corvana see images uploaded
Nice to have
• added tag lines or statements to re-enforce the focus of the luxury traveler that has earned that status of an elite flyer and traveler. We are open to any text or tag line ideas.
Should not have
• Clip-art of any kind.

```html
<!DOCTYPE html>
<html lang="en">
<head>
<meta charset="utf-8">
<title>Velvet Horizon Voyages Inc. – Business Card</title>
<link rel="stylesheet" href="https://fonts.googleapis.com/css2?family=Cinzel:wght@600;700&family=Source+Sans+3:wght@400&family=Kaushan+Script&display=swap">
<style>
  :root {
    --backdrop: #6e6e6e;
    --card-dark: #1f1e1e;
    --gold: #e0b93a;
    --gold-soft: #d8ad3c;
    --text-light: #f2f2f2;
    --band-white: #ffffff;
    --supplier-teal: #1b8fa6;
    --sky-top: #1d3f8a;
    --sky-mid: #5e8fd0;
    --sea: #3fb7c4;
    --pool: #2a9fb0;
  }
  * { margin: 0; padding: 0; box-sizing: border-box; }
  html, body { width: 1200px; height: 900px; overflow: hidden; }
  body {
    background: var(--backdrop);
    position: relative;
    font-family: "Source Sans 3", "Helvetica Neue", Arial, sans-serif;
  }
  .card {
    position: absolute;
    top: 276px;
    width: 477px;
    height: 294px;
    overflow: hidden;
    box-shadow: 3px 4px 8px rgba(0,0,0,0.35);
  }
  .card-front {
    left: 116px;
    background: var(--card-dark);
    border-radius: 0 46px 0 46px;
    color: var(--text-light);
  }
  .holder-name {
    position: absolute;
    left: 29px; top: 20px;
    font-family: "Cinzel", Georgia, serif;
    font-weight: 700;
    font-size: 17px;
    color: var(--gold);
  }
  .holder-title {
    position: absolute;
    left: 29px; top: 43px;
    font-size: 13px;
  }
  .company-name {
    position: absolute;
    left: 32px; top: 114px;
    font-family: "Cinzel", Georgia, serif;
    font-weight: 600;
    font-size: 18px;
    color: var(--gold);
    display: flex; align-items: center; gap: 10px;
  }
  .company-name .mark {
    width: 12px; height: 12px;
    border-radius: 50%;
    background: var(--gold);
  }
  .contact-list {
    position: absolute;
    right: 20px; top: 182px;
    list-style: none;
    text-align: right;
    font-size: 13px;
    line-height: 20px;
  }
  .contact-list li { display: flex; justify-content: flex-end; align-items: center; gap: 8px; }
  .contact-list svg { width: 11px; height: 11px; fill: var(--gold-soft); }
  .address {
    position: absolute;
    right: 20px; top: 247px;
    font-size: 13px;
  }
  .card-back {
    left: 622px;
    border-radius: 46px 0 46px 0;
    background: var(--pool);
  }
  .scene-photo {
    position: absolute; inset: 0;
    background: linear-gradient(180deg, var(--sky-top) 0%, var(--sky-mid) 40%, #cfe3f2 48%, var(--sea) 52%, var(--pool) 100%);
  }
  .back-brand {
    position: absolute;
    left: 70px; top: 62px;
    font-family: "Cinzel", Georgia, serif;
    font-weight: 700;
    font-size: 22px;
    color: var(--gold);
  }
  .supplier-band {
    position: absolute;
    left: 0; right: 0; top: 221px;
    height: 58px;
    background: var(--band-white);
    display: flex; align-items: center; justify-content: center;
  }
  .supplier-name {
    font-family: "Kaushan Script", cursive;
    font-size: 30px;
    color: var(--supplier-teal);
  }
</style>
</head>
<body>
  <section class="card card-front" aria-label="Business card front">
    <h1 class="holder-name">Kdelane</h1>
    <p class="holder-title">Managing Director</p>
    <div class="company-name"><span class="mark"></span>Velvet Horizon Voyages Inc.</div>
    <ul class="contact-list">
      <li>(403)271-4408
        <svg viewBox="0 0 24 24" aria-hidden="true"><path d="M6.6 10.8a15.1 15.1 0 0 0 6.6 6.6l2.2-2.2a1 1 0 0 1 1-.25 11.4 11.4 0 0 0 3.6.57 1 1 0 0 1 1 1V20a1 1 0 0 1-1 1A17 17 0 0 1 3 4a1 1 0 0 1 1-1h3.5a1 1 0 0 1 1 1c0 1.25.2 2.45.57 3.57a1 1 0 0 1-.25 1z"/></svg>
      </li>
      <li>kdelane@velvethorizonvoyages.com
        <svg viewBox="0 0 24 24" aria-hidden="true"><path d="M2 5h20v14H2z M3 6l9 7 9-7" stroke="#1f1e1e" stroke-width="1.6"/></svg>
      </li>
      <li>www.velvethorizonvoyages.com
        <svg viewBox="0 0 24 24" aria-hidden="true"><circle cx="12" cy="12" r="10"/><path d="M2 12h20M12 2c3 3 3 17 0 20M12 2c-3 3-3 17 0 20" stroke="#1f1e1e" stroke-width="1.5" fill="none"/></svg>
      </li>
    </ul>
    <p class="address">212 Pinecrest Hollow Rd NW Calgary, Alberta T2K 4W9 Canada</p>
  </section>

  <section class="card card-back" aria-label="Business card back">
    <div class="scene-photo" role="img" aria-label="Photo of a luxury resort infinity pool with beach umbrellas and loungers by a turquoise sea under a blue sky"></div>
    <div class="back-brand">Velvet Horizon Voyages</div>
    <div class="supplier-band"><span class="supplier-name">Corvana</span></div>
  </section>
</body>
</html>
```